Elevated, strategic rebranding needed! Larkfield Terrace Brochure

This is a rebranding project and we need flyers to use for marketing materials to physicians, case managers, families, and hospitals. Tamarind Unified Wellness just acquired this massive, gorgeous campus and we need to rebrand now! The public has known this as Meridian Holloway Grove since 2008. It has been stuck in its ways (albeit it has had a strong reputation) for years. We are bringing them into the new world of senior care! Larkfield Terrace is redefining senior care in Ponca City, Oklahoma. As part of Tamarind Unified Wellness, we're breaking away from the community's legacy as a traditional Catholic nonprofit to become an exciting, energetic, and extraordinary campus where exceptional care meets genuine innovation. We offer a full continuum of living options—independent living, assisted living, memory care, skilled nursing, and long-term care—with an integrated approach that addresses every aspect of our residents' lives: mental, physical, spiritual, and psychosocial wellness. Through strategic partnerships with best-in-class ancillary providers and our holistic care philosophy, we deliver coordinated, comprehensive care that honors aging adults and empowers them at every level. We are creating a community where remarkable outcomes happen every day. We need marketing materials that capture this energy, sophistication, and forward-thinking approach as we introduce Ponca City to the new Larkfield Terrace. Our website is just a splash page at www.larkfieldterrace-example.com and our parent company is Tamarind Unified Wellness. www.tamarinduw-example.com
We want Larkfield to stand alone but wanted you to read about our vision and mission at Tamarind.

Target Market(s)

Senior Healthcare, hospitals, physicians, families

Industry/Entity Type

Healthcare

Requirements
Must have
• multicultural representation, emphasis on quality and purpose for seniors; every level of care; stunning campus; friendships, community, culture, health
Nice to have
• pictures that are not on every person's websites, pictures of different levels of health but still dignified,
Should not have
• should not make aging adults appear helpless, frail, and sad.

```html
<!DOCTYPE html>
<html lang="en">
<head>
<meta charset="utf-8">
<title>Larkfield Terrace Flyer</title>
<link href="https://fonts.googleapis.com/css2?family=Figtree:wght@400;500;700;800&family=Josefin+Sans:wght@300;700&display=swap" rel="stylesheet">
<style>
:root{
  --page:#e4e4e4;
  --black:#050505;
  --gold:#d2b065;
  --gold-light:#e6cb86;
  --gold-deep:#b8934a;
  --band:#3a3a3d;
  --white:#ffffff;
  --ink:#111111;
}
*{margin:0;padding:0;box-sizing:border-box}
html,body{width:1200px;height:1117px;overflow:hidden;background:var(--page)}
.flyer{position:absolute;left:220px;top:20px;width:760px;height:1076px;background:var(--black);overflow:hidden;font-family:"Figtree",sans-serif;color:var(--white)}
.header{position:absolute;left:0;top:0;width:760px;height:124px;background:var(--black)}
.brand-mark{position:absolute;left:64px;top:20px;width:86px;height:86px;border-radius:50%;background:radial-gradient(circle at 35% 30%,var(--gold-light),var(--gold-deep))}
.brand-name{position:absolute;left:175px;top:30px;font-family:"Josefin Sans",sans-serif;font-weight:300;font-size:34px;letter-spacing:7px;color:var(--gold);white-space:nowrap}
.brand-tag{position:absolute;left:176px;top:73px;font-family:"Josefin Sans",sans-serif;font-weight:700;font-size:13px;letter-spacing:4.3px;color:var(--gold);white-space:nowrap}
.hero-photo{position:absolute;left:0;top:124px;width:760px;height:480px;background:linear-gradient(120deg,#b89776 0%,#d4ae82 40%,#9b7550 75%,#c9a77f 100%)}
.service-box{position:absolute;left:401px;top:560px;width:328px;height:401px;border:3px solid var(--gold);border-top:none;border-radius:0 0 28px 28px}
.waves{position:absolute;left:0;top:0}
.hero-title{position:absolute;left:300px;width:446px;top:400px;text-align:center;font-weight:700;font-size:27.5px;line-height:30px;text-transform:uppercase;color:var(--white)}
.hero-intro{position:absolute;left:320px;width:406px;top:502px;text-align:center;font-weight:500;font-size:14.4px;line-height:18px}
.vision{position:absolute;left:64px;top:602px;width:320px}
.vision-title{font-weight:800;font-size:24.5px;line-height:28px;text-transform:uppercase}
.vision-title .accent{color:var(--gold)}
.vision p{font-size:14px;line-height:16.6px;margin-top:12px;font-weight:400}
.vision p.closing{font-weight:700;margin-top:17px}
.service-list{position:absolute;left:434px;top:641px;list-style:none}
.service{display:flex;align-items:center;height:54px;margin-bottom:6.7px}
.service-icon{width:54px;height:54px;border-radius:50%;background:radial-gradient(circle at 35% 30%,var(--gold-light),var(--gold-deep));flex:none}
.service-name{margin-left:13px;font-weight:700;font-size:21.5px}
.contact{position:absolute;left:0;top:978px;width:760px;height:98px;background:var(--white);color:var(--ink)}
.phone{position:absolute;left:64px;top:22px;display:flex;align-items:center;font-weight:700;font-size:41px}
.phone svg{margin-right:8px}
.divider{position:absolute;left:419px;top:26px;width:1px;height:44px;background:var(--gold)}
.web{position:absolute;left:429px;top:20px;font-size:17.5px;line-height:24px;list-style:none}
.web li{display:flex;align-items:center}
.web .dot{width:12px;height:12px;border-radius:50%;background:var(--gold);margin-right:8px}
</style>
</head>
<body>
<main class="flyer">
  <header class="header">
    <div class="brand-mark"></div>
    <div class="brand-name">LARKFIELD TERRACE</div>
    <div class="brand-tag">INTEGRATED HEALTHCARE</div>
  </header>

  <div class="hero-photo" role="img" aria-label="Photo of a diverse group of smiling senior friends taking a selfie together on a sunny terrace"></div>

  <div class="service-box"></div>

  <svg class="waves" width="760" height="1076" viewBox="0 0 760 1076" aria-hidden="true">
    <defs>
      <linearGradient id="goldFill" x1="0" y1="0" x2="1" y2="1">
        <stop offset="0" stop-color="#d7b66d"/>
        <stop offset="1" stop-color="#c6a256"/>
      </linearGradient>
    </defs>
    <path d="M0,555 C150,500 330,540 500,590 C620,625 720,600 760,565 L760,600 C720,640 620,655 500,625 C330,580 150,545 0,590 Z" fill="var(--band)"/>
    <path d="M0,598 C150,553 330,588 500,633 C620,663 720,648 760,608 L760,640 L0,640 Z" fill="var(--black)"/>
    <path d="M0,480 C60,510 130,520 200,505 C300,485 370,420 450,380 C530,340 580,345 640,350 C700,355 740,370 760,375 L760,565 C720,600 620,625 500,590 C330,540 150,500 0,555 Z" fill="url(#goldFill)"/>
    <path d="M0,555 C150,500 330,540 500,590 C620,625 720,600 760,565" fill="none" stroke="var(--white)" stroke-width="4"/>
  </svg>

  <h1 class="hero-title">Living choices<br>with differing levels<br>of care to suit your needs</h1>
  <p class="hero-intro">Larkfield Terrace is an active retirement community with independent, assisted, skilled nursing and rehabilitation care options.</p>

  <section class="vision">
    <h2 class="vision-title">We are bringing<br><span class="accent">into the new world<br>of senior care!</span></h2>
    <p>We offer a full continuum of living options—independent living, assisted living, memory care, skilled nursing, and long-term care with an integrated approach that addresses every aspect of our residents' lives: mental, physical, spiritual, and psychosocial wellness.</p>
    <p>Through strategic partnerships with best-in-class ancillary providers and our holistic care philosophy, we deliver coordinated, comprehensive care that honors aging adults and empowers them at every level.</p>
    <p class="closing">We are creating a community where remarkable outcomes happen every day.</p>
  </section>

  <ul class="service-list">
    <li class="service"><span class="service-icon"></span><span class="service-name">Independent Living</span></li>
    <li class="service"><span class="service-icon"></span><span class="service-name">Assisted Living</span></li>
    <li class="service"><span class="service-icon"></span><span class="service-name">Memory Care</span></li>
    <li class="service"><span class="service-icon"></span><span class="service-name">Skilled Nursing</span></li>
    <li class="service"><span class="service-icon"></span><span class="service-name">Long-Term Care</span></li>
  </ul>

  <footer class="contact">
    <div class="phone">
      <svg width="28" height="40" viewBox="0 0 28 40" aria-hidden="true"><path d="M6,2 L12,2 L14,12 L9,15 C10,22 13,28 18,32 L23,29 L27,35 L23,39 C12,38 2,24 2,8 Z" fill="var(--gold)"/></svg>
      (580) 555-0142
    </div>
    <div class="divider"></div>
    <ul class="web">
      <li><span class="dot"></span>info@larkfieldterrace.com</li>
      <li><span class="dot"></span>larkfieldterrace.com</li>
    </ul>
  </footer>
</main>
</body>
</html>
```